* see below *
Project: Stationary for Law Firm
Stationary for Law Firm - Law
Stationary for Law Firm
Use standard fonts
Dorian Valesko, Esq.
Managing Partner
4382 Linden Terrace Brooklyn, New York 11356
dorian@valeskolegal.com
www.ValeskoLegal.com
This is a design for a stationary, not for a business card.
DorianValesko DorianValesko
This is a design for a stationary, not for a business card. I need a design for a letterhead stationary

```html
<!DOCTYPE html>
<html lang="en">
<head>
<meta charset="utf-8">
<title>Dorian Valesko, LLP — Stationery</title>
<link href="https://fonts.googleapis.com/css2?family=Cinzel:wght@400;600&family=Open+Sans:wght@400;600&display=swap" rel="stylesheet">
<style>
  :root{
    --maroon:#7d1a26;
    --grey:#6e6e70;
    --paper:#ffffff;
    --backdrop:#eef0f1;
    --ink:#3a3a3a;
    --serif:'Cinzel', Georgia, serif;
    --sans:'Open Sans', Arial, sans-serif;
  }
  *{box-sizing:border-box;margin:0;padding:0}
  html,body{width:1200px;height:936px;overflow:hidden;background:var(--backdrop)}
  .canvas{position:relative;width:1200px;height:936px}
  .sheet{position:absolute;background:var(--paper);overflow:hidden}
  .band{position:absolute;left:0;right:0;background:linear-gradient(180deg,var(--grey) 0%,var(--maroon) 35%,var(--maroon) 100%)}
  .band-top{background:linear-gradient(0deg,var(--grey) 0%,var(--maroon) 35%,var(--maroon) 100%)}
  .mark{display:inline-block;background:var(--maroon)}
  .brand{font-family:var(--serif);color:var(--maroon);font-weight:600;white-space:nowrap}
  .tagline{font-family:var(--serif);color:var(--grey);letter-spacing:.18em;white-space:nowrap;text-transform:uppercase}
  .web{position:absolute;font-family:var(--sans);color:#fff;letter-spacing:.08em;white-space:nowrap}

  /* letterhead */
  .letterhead{left:114px;top:63px;width:464px;height:559px}
  .letterhead .band{top:430px;bottom:0}
  .letterhead .logo{position:absolute;left:40px;top:36px}
  .letterhead .logo .mark{width:34px;height:34px}
  .letterhead .logo .brand{font-size:11px;margin-top:4px}
  .letterhead .logo .tagline{font-size:5px}
  .letter-body{position:absolute;left:40px;top:112px;width:384px;font-family:var(--sans);font-size:5.6px;line-height:1.55;color:var(--ink)}
  .letter-body p{margin-bottom:8px}
  .signature{width:46px;height:16px;background:linear-gradient(90deg,#d9d9d9,#bdbdbd);margin:4px 0 6px}
  .contact{position:absolute;left:300px;top:474px;list-style:none;font-family:var(--sans);font-size:6px;color:#fff;line-height:1}
  .contact li{display:flex;align-items:center;gap:5px;margin-bottom:5px;white-space:nowrap}
  .contact .dot{width:7px;height:7px;border-radius:50%;background:#fff;flex:none}

  /* folder */
  .folder{left:634px;top:38px;width:462px;height:584px}
  .folder .band{top:420px;bottom:0}
  .folder .logo{position:absolute;left:0;right:0;top:190px;text-align:center}
  .folder .logo .mark{width:84px;height:84px}
  .folder .logo .brand{font-size:26px;margin-top:14px}
  .folder .logo .tagline{font-size:10px;margin-top:4px;border-top:1px solid var(--grey);border-bottom:1px solid var(--grey);display:inline-block;padding:2px 10px}
  .folder .web{left:24px;top:556px;font-size:9px}

  /* business cards */
  .card{width:211px;height:104px}
  .card-front{left:43px;top:655px}
  .card-front .band{top:64px;bottom:0}
  .card-back{left:43px;top:774px}
  .card .logo{position:absolute;left:0;right:0;text-align:center}
  .card-front .logo{top:8px}
  .card-back .logo{top:24px}
  .card .logo .mark{width:22px;height:22px}
  .card .logo .brand{font-size:7.5px;margin-top:3px}
  .card .logo .tagline{font-size:3.6px}

  /* envelope */
  .envelope{left:274px;top:655px;width:449px;height:220px}
  .envelope .band{top:150px;bottom:0}
  .envelope .logo{position:absolute;left:22px;top:16px;text-align:left}
  .envelope .logo .mark{width:34px;height:34px}
  .envelope .logo .brand{font-size:10px;margin-top:4px}
  .envelope .logo .tagline{font-size:4.6px}
  .envelope .web{left:0;right:0;text-align:center;top:199px;font-size:8px}
  .envelope-back{left:743px;top:665px;width:411px;height:210px}
  .envelope-back .band{top:0;height:70px}
  .envelope-back .web{left:0;right:0;top:18px;text-align:center;font-size:8px}
</style>
</head>
<body>
<main class="canvas">

  <section class="sheet letterhead">
    <div class="band" role="img" aria-label="Maroon and grey decorative band along the foot of the page"></div>
    <div class="logo">
      <span class="mark"></span>
      <div class="brand">Dorian Valesko, LLP</div>
      <div class="tagline">Attorneys at Law</div>
    </div>
    <div class="letter-body">
      <p>June 4, 2024<br>Client Name<br>Street Address, City, State</p>
      <p>Dear Client,</p>
      <p>Thank you for choosing our firm to represent you in this matter. We have reviewed the documents you provided and will prepare a full summary of our findings for your review within the coming weeks.</p>
      <p>Please gather any further records related to the case and send them to our office at your convenience so that we can proceed without delay.</p>
      <p>Should you have any questions about the next steps, our team is available to meet with you in person or by phone during regular business hours.</p>
      <p>Best Regards,</p>
      <div class="signature" role="img" aria-label="Handwritten signature"></div>
      <p>Dorian Valesko, Esq.<br>Managing Partner</p>
    </div>
    <ul class="contact">
      <li><span class="dot"></span>4382 Linden Terrace Brooklyn, New York 11356</li>
      <li><span class="dot"></span>(718) 555-0142</li>
      <li><span class="dot"></span>dorian@valeskolegal.com</li>
      <li><span class="dot"></span>www.ValeskoLegal.com</li>
    </ul>
  </section>

  <section class="sheet folder">
    <div class="band" role="img" aria-label="Maroon and grey decorative band along the foot of the folder"></div>
    <div class="logo">
      <span class="mark"></span>
      <div class="brand">Dorian Valesko, LLP</div>
      <div class="tagline">Attorneys at Law</div>
    </div>
    <div class="web">www.ValeskoLegal.com</div>
  </section>

  <section class="sheet card card-front">
    <div class="band" role="img" aria-label="Maroon and grey decorative band along the foot of the card"></div>
    <div class="logo">
      <span class="mark"></span>
      <div class="brand">Dorian Valesko, LLP</div>
      <div class="tagline">Attorneys at Law</div>
    </div>
  </section>

  <section class="sheet card card-back">
    <div class="logo">
      <span class="mark"></span>
      <div class="brand">Dorian Valesko, LLP</div>
      <div class="tagline">Attorneys at Law</div>
    </div>
  </section>

  <section class="sheet envelope">
    <div class="band" role="img" aria-label="Maroon and grey decorative band along the foot of the envelope"></div>
    <div class="logo">
      <span class="mark"></span>
      <div class="brand">Dorian Valesko, LLP</div>
      <div class="tagline">Attorneys at Law</div>
    </div>
    <div class="web">www.ValeskoLegal.com</div>
  </section>

  <section class="sheet envelope-back">
    <div class="band band-top" role="img" aria-label="Maroon and grey decorative band across the envelope flap"></div>
    <div class="web">www.ValeskoLegal.com</div>
  </section>

</main>
</body>
</html>
```